IT Services company requires a services website design with integrated blog

We at Brambleway Code Haulage primarily provide application migration consultancy (e.g. moving applications from Paneview QR to Paneview 5) and application virtualization (e.g. Dunmore Box-K) consultancy.This process is commonly known as 'packaging' but doesnt involve cardboard boxes ;) (however, I am happy to use that visual analogy if you want to use any box graphics) We also provide application compatibility testing, software auditing and application portfolio management.

We are looking for a complete redesign of our current horrible diy attempt at a website at www.brambleway-example.com. We have had created a rebranded logo (attached files and fonts) and a rebranded business card (also attached) We would like the website to match the same/similar colors and styling as these.

I want to redisgn the website so that the main focus of this website is to show our subject matter expertise with a blog and should take up most of the websites real estate and focus on the home screen. Then if the customer wants, they can use our services to help them in their own application migration/deployment projects by browsing our details in links/buttons somewhere

In any of the designs, please do not include my Velharo or Dunmore partnerships.  Thank you

Target Market(s)

Application packagers / engineers looking for technical articles

Application migration project managers

Industry/Entity Type

Real Estate

Requirements
Must have
• This site is primarily a blog site. The blog should have buttons to share each article on social media site. It should be easy for me to create or edit new blog articles (have technical skills but not creative ones). Each article should also allow for comments (do not require approval but should allow for admin removal) but do not add like/vote buttons because i do not expect large enough traffic and could be determental.

There should be a contact page to host contact information and an email box that goes to enquiries@brambleway-example.com

The other pages should include About us and Services (placeholder text to be used as current site text needs overhauling but original text can be used in the design just remember when placing that the text may shorten or increase etc.)

All text has to be easily editable (no over use of text in images where possible)
Nice to have
• An email notification of new comments to articles sent to webadmin@brambleway-example.com

Newsletter subscription
Should not have
• Do not include vote/like buttons or website counters. Initial traffic is not going to be large enough to warrant these features and may reflect badly on the site.

No logon features. Site content and commenting should be open access

No opinion polls

No why choose us section from current website

Do not include partner information in new site (Velharo and Dunmore)

DO NOT JUST REPLICATE EXISTING WEBSITE FEATURES, PLEASE REFER TO THIS BRIEF. THIS SITE NEEDS TO PRIMARILY BE A BLOG

```html
<!DOCTYPE html>
<html lang="en">
<head>
<meta charset="utf-8">
<title>Brambleway Code Haulage — Magazine</title>
<link rel="stylesheet" href="https://fonts.googleapis.com/css2?family=Questrial&family=Mulish:wght@400;700;800&family=Righteous&display=swap">
<style>
  :root {
    --paper: #eeeeee;
    --panel: #fafafa;
    --ink: #222222;
    --grey: #6b6b6b;
    --grey-soft: #9a9a9a;
    --grey-pale: #bdbdbd;
    --green: #66cc00;
    --navy: #0a1a6e;
    --blue: #1d2fb8;
    --yellow: #f2c51c;
    --footer: #0036a0;
    --pattern-a: #1b5fc9;
    --pattern-b: #8fd0f2;
  }
  * { box-sizing: border-box; margin: 0; padding: 0; }
  html, body { width: 1000px; height: 1200px; overflow: hidden; }
  body { background: var(--paper); font-family: "Questrial", sans-serif; color: var(--ink); position: relative; }
  .abs { position: absolute; }
  a { color: inherit; text-decoration: none; }

  .corner-pattern { left: 0; top: 0; width: 540px; height: 235px; }
  .main-nav a { position: absolute; top: 52px; font-family: "Mulish", sans-serif; font-weight: 700; font-size: 26px; color: var(--grey); letter-spacing: .5px; }
  .main-nav .current { color: var(--green); }

  .brand { left: 372px; top: 112px; display: flex; align-items: center; gap: 14px; }
  .brand-mark { width: 74px; height: 74px; border-radius: 50%; background: var(--blue); }
  .brand-name { font-family: "Questrial", sans-serif; font-size: 30px; line-height: 34px; color: var(--grey); width: 250px; }

  .service { font-family: "Righteous", sans-serif; font-size: 28px; line-height: 36px; letter-spacing: 1px; }
  .service.muted { color: var(--grey); }
  .service.active { color: var(--ink); }
  .service.pale { color: var(--grey-pale); }
  .rule { background: var(--green); }

  .content-panel { left: 47px; top: 492px; width: 903px; height: 611px; background: var(--panel); }
  .tabs a { position: absolute; top: 506px; font-family: "Mulish", sans-serif; font-weight: 700; font-size: 20px; color: var(--grey-soft); }
  .tabs .current { color: var(--navy); }
  .tab-sep { top: 497px; width: 0; height: 46px; border-left: 1px dotted var(--grey-pale); }
  .contact-mail { left: 621px; top: 508px; font-size: 19px; color: var(--ink); }

  .post-icon { width: 52px; height: 52px; border-radius: 50%; background: #3d3d45; }
  .post-icon.square { border-radius: 4px; width: 30px; height: 30px; background: #d8306a; }
  .post-title { left: 171px; width: 450px; font-family: "Mulish", sans-serif; font-weight: 700; font-size: 22px; line-height: 36px; color: var(--grey); }
  .post-date { right: 295px; font-size: 14px; color: var(--grey-pale); }
  .post-body { left: 120px; width: 583px; font-size: 12.5px; line-height: 18px; color: var(--grey); text-align: justify; }
  .read-more { left: 644px; width: 57px; height: 23px; border: 1.5px solid var(--green); border-radius: 4px; color: var(--green); font-family: "Mulish", sans-serif; font-weight: 800; font-size: 11px; letter-spacing: 1.5px; text-align: center; line-height: 20px; }
  .comment-count { left: 52px; width: 60px; text-align: center; font-size: 9px; color: var(--grey-soft); }
  .comment-bubble { left: 73px; width: 20px; height: 16px; }

  .sidebar-line { background: #c8c8c8; }
  .search-box { left: 758px; top: 592px; width: 104px; height: 21px; border: 1px solid #cfe9b0; font-size: 12px; color: #c4c4c4; padding: 2px 7px; background: #fff; }
  .search-btn { left: 864px; top: 588px; width: 50px; height: 27px; border: 1px solid #bbb; border-radius: 3px; background: #fff; }
  .sidebar-title { left: 759px; top: 696px; font-size: 26px; color: #333; letter-spacing: .5px; }
  .category-list a { position: absolute; left: 759px; font-size: 19px; letter-spacing: .5px; }
  .category-list a:nth-child(odd) { color: #333; }
  .category-list a:nth-child(even) { color: #777; }

  .site-footer { left: 0; top: 1103px; width: 1000px; height: 80px; background: var(--footer); }
  .site-footer a { position: absolute; color: #fff; font-size: 16px; }
  .site-footer .current { font-family: "Mulish", sans-serif; font-weight: 700; }
  .footer-pattern { left: 0; top: 1180px; width: 1000px; height: 20px; }
</style>
</head>
<body>

<svg class="abs corner-pattern" viewBox="0 0 540 235" role="img" aria-label="Decorative blue geometric pattern">
  <defs>
    <linearGradient id="cornerFill" x1="0" y1="0" x2="1" y2="1">
      <stop offset="0" stop-color="var(--pattern-a)"/>
      <stop offset="1" stop-color="var(--pattern-b)"/>
    </linearGradient>
  </defs>
  <polygon points="0,0 532,0 0,232" fill="url(#cornerFill)"/>
</svg>

<nav class="main-nav">
  <a href="#" style="left:415px">About Us</a>
  <a href="#" style="left:613px">Our Services</a>
  <a href="#" class="current" style="left:840px">Contact</a>
</nav>

<div class="abs brand">
  <div class="brand-name">Brambleway<br>Code Haulage</div>
  <div class="brand-mark"></div>
</div>

<section class="service-grid">
  <div class="abs service muted" style="left:122px;top:236px">Application<br>migration<br>consultancy</div>
  <div class="abs" style="left:351px;top:247px;width:2px;height:109px;background:var(--blue)"></div>
  <div class="abs service active" style="left:431px;top:236px">Application<br>virtualization<br>consultancy</div>
  <div class="abs" style="left:702px;top:247px;width:2px;height:109px;background:var(--yellow)"></div>
  <div class="abs service pale" style="left:757px;top:236px">Application<br>compatibility<br>testing</div>
  <div class="abs rule" style="left:50px;top:355px;width:900px;height:2px"></div>
  <div class="abs rule" style="left:499px;top:356px;width:2px;height:112px"></div>
  <div class="abs service muted" style="left:120px;top:375px;line-height:54px">Application Portofolio<br>Management</div>
  <div class="abs service muted" style="left:614px;top:375px;line-height:54px">Software<br>Auditing</div>
</section>

<div class="abs content-panel"></div>

<nav class="tabs">
  <a href="#" class="current" style="left:65px">Magazine</a>
  <span class="abs tab-sep" style="left:179px"></span>
  <a href="#" style="left:210px">Category 1</a>
  <span class="abs tab-sep" style="left:351px"></span>
  <a href="#" style="left:378px">Category 2</a>
</nav>
<svg class="abs" style="left:564px;top:506px" width="42" height="30" viewBox="0 0 42 30" aria-hidden="true">
  <rect x="1" y="1" width="40" height="28" fill="#f7f7f7" stroke="#bbb"/>
  <polyline points="1,1 21,17 41,1" fill="none" stroke="#bbb"/>
</svg>
<div class="abs contact-mail">enquiries@brambleway-example.com</div>

<!-- Post 1 -->
<div class="abs post-icon" style="left:66px;top:602px"></div>
<h2 class="abs post-title" style="top:590px">How To Run Local Applications Within an Box-K 5 Sequence</h2>
<div class="abs post-date" style="top:638px">june 8 2013</div>
<svg class="abs comment-bubble" style="top:688px" viewBox="0 0 20 16" aria-hidden="true"><ellipse cx="10" cy="7" rx="9" ry="6" fill="#ddd"/><polygon points="4,11 3,16 9,12" fill="#ddd"/></svg>
<div class="abs comment-count" style="top:714px">(3) comments</div>
<p class="abs post-body" style="top:668px">Those of us that are used to Box-K before version 5 may be used to using the Boxtray.exe with the /exe switch to run a command within the box-k sequence.&nbsp; With Box-K 5 this has now gone. Instead Box-K 5 is Shellwork driven and there is a new cmdlet to achieve the same result.&nbsp; To do this you now run the following Shellwork cmdlets (this example executes jotter.exe within the My Application sequence):</p>
<a href="#" class="abs read-more" style="top:749px">READ</a>

<!-- Post 2 -->
<div class="abs post-icon square" style="left:66px;top:783px"></div>
<h2 class="abs post-title" style="top:773px">What is a Package Accelerator?</h2>
<div class="abs post-date" style="top:804px">june 8 2013</div>
<svg class="abs comment-bubble" style="top:852px" viewBox="0 0 20 16" aria-hidden="true"><ellipse cx="10" cy="7" rx="9" ry="6" fill="#ddd"/><polygon points="4,11 3,16 9,12" fill="#ddd"/></svg>
<div class="abs comment-count" style="top:878px">(1) comments</div>
<p class="abs post-body" style="top:831px">Those of us that are used to Box-K before version 5 may be used to using the Boxtray.exe with the /exe switch to run a command within the box-k sequence.&nbsp; With Box-K 5 this has now gone. Instead Box-K 5 is Shellwork driven and there is a new cmdlet to achieve the same result.&nbsp; To do this you now run the following Shellwork cmdlets (this example executes jotter.exe within the My Application sequence):</p>
<a href="#" class="abs read-more" style="top:912px">READ</a>

<!-- Post 3 -->
<div class="abs post-icon square" style="left:66px;top:967px;background:#e0306a"></div>
<h2 class="abs post-title" style="top:944px">Box-K Command Line Interface</h2>
<div class="abs post-date" style="top:976px">june 8 2013</div>
<svg class="abs comment-bubble" style="top:1018px" viewBox="0 0 20 16" aria-hidden="true"><ellipse cx="10" cy="7" rx="9" ry="6" fill="#ddd"/><polygon points="4,11 3,16 9,12" fill="#ddd"/></svg>
<div class="abs comment-count" style="top:1043px">(0) comments</div>
<p class="abs post-body" style="top:1000px">Those of us that are used to Box-K before version 5 may be used to using the Boxtray.exe with the /exe switch to run a command within the box-k sequence.&nbsp; With Box-K 5 this has now gone. Instead Box-K 5 is Shellwork driven and there is a new cmdlet to achieve the same result.&nbsp; To do this you now run the following Shellwork cmdlets (this example executes jotter.exe within the My Application sequence):</p>
<a href="#" class="abs read-more" style="top:1077px">READ</a>

<!-- Sidebar -->
<aside>
  <div class="abs sidebar-line" style="left:736px;top:578px;width:2px;height:500px"></div>
  <div class="abs sidebar-line" style="left:737px;top:578px;width:177px;height:1px"></div>
  <div class="abs sidebar-line" style="left:737px;top:622px;width:177px;height:1px"></div>
  <div class="abs search-box">Custom search</div>
  <div class="abs search-btn">
    <svg width="48" height="25" viewBox="0 0 48 25" aria-hidden="true"><polyline points="17,13 22,18 32,7" fill="none" stroke="var(--green)" stroke-width="3"/></svg>
  </div>
  <h3 class="abs sidebar-title" style="font-weight:400">Articles</h3>
  <nav class="category-list">
    <a href="#" style="top:757px">Category</a>
    <a href="#" style="top:806px">Category</a>
    <a href="#" style="top:854px">Category</a>
    <a href="#" style="top:903px">Category</a>
    <a href="#" style="top:952px">Category</a>
    <a href="#" style="top:1001px">Category</a>
  </nav>
</aside>

<footer class="abs site-footer">
  <a href="#" style="left:48px;top:15px">Our Services</a>
  <a href="#" style="left:48px;top:53px">About Us</a>
  <a href="#" style="left:198px;top:15px">Blog</a>
  <a href="#" class="current" style="left:200px;top:53px">Contact</a>
</footer>
<svg class="abs footer-pattern" viewBox="0 0 1000 20" preserveAspectRatio="none" role="img" aria-label="Decorative blue geometric pattern strip">
  <defs>
    <linearGradient id="stripFill" x1="0" y1="0" x2="1" y2="0">
      <stop offset="0" stop-color="var(--pattern-b)"/>
      <stop offset="1" stop-color="var(--pattern-a)"/>
    </linearGradient>
  </defs>
  <rect width="1000" height="20" fill="var(--paper)"/>
  <polygon points="0,20 1000,0 1000,20" fill="url(#stripFill)"/>
</svg>

</body>
</html>
```